Software Company Business Card Design

We are looking for a business card design for a software, messaging & IT services company based in Australia.

Talvora Group is the holding company for 3 brands all offering technology based business solutions; Talvora, Brindle & Quillpad. Brand Identity = Friendly, Professional, Viable, Vibrant, Creative

We want our business card to reflect that we are an innovative market leader. The design should be clean, professional and original.

This design will be used for all 3 brands.

More information about our company can be found at: www.talvoragroup.example.au
www.brindle.example.au

Details we would like on the card:

Firstname Lastname
Position
Level 17, 482 Ormond Rd
North Sydney
NSW 2060
Phone: +61 2 5550 1738
Fax: +61 2 5550 1794
Mobile:
Email:
www.talvoragroup.example.au

Target Market(s)

Our business cards are given to B2B and industry professionals.

Industry/Entity Type

Business

Requirements
Must have
• The Business Card must include the same colours as the logo.
Nice to have
• We would like it to me double sided.

```html
<!DOCTYPE html>
<html lang="en">
<head>
<meta charset="utf-8">
<title>Talvora Group – Business Cards</title>
<link rel="stylesheet" href="https://fonts.googleapis.com/css2?family=Nunito:wght@400;800&display=swap">
<style>
  :root {
    --crimson: #b0103a;
    --lavender: #9c9eba;
    --blush: #f2d5d3;
    --ink-soft: #9d9daa;
    --paper: #ffffff;
    --stage: #ffffff;
  }
  * { box-sizing: border-box; margin: 0; padding: 0; }
  html, body { width: 1200px; height: 900px; overflow: hidden; background: var(--stage); }
  body { position: relative; font-family: "Nunito", Arial, sans-serif; }

  .card {
    position: absolute;
    width: 520px;
    height: 330px;
    overflow: hidden;
    box-shadow: 3px 4px 10px rgba(0,0,0,0.22);
  }
  .card--front { background: var(--paper); }
  .card--back { background: var(--crimson); }

  .card--talvora-front  { left: 70px;  top: 74px;  transform: rotate(-1deg); }
  .card--talvora-back   { left: 630px; top: 80px;  transform: rotate(7deg); }
  .card--quillpad-front { left: 64px;  top: 500px; transform: rotate(-8deg); }
  .card--quillpad-back  { left: 620px; top: 505px; width: 560px; height: 365px; }

  .backdrop { position: absolute; inset: 0; }
  .backdrop--front {
    background: radial-gradient(ellipse 70% 80% at 58% 62%, var(--paper) 14%, var(--blush) 60%, var(--paper) 100%);
  }
  .backdrop--back {
    background: radial-gradient(ellipse 75% 85% at 42% 100%, var(--crimson) 38%, var(--lavender) 95%);
  }

  .brand {
    position: absolute;
    font-weight: 800;
    color: var(--crimson);
    line-height: 0.9;
    letter-spacing: -1px;
    white-space: nowrap;
  }
  .brand__sub {
    display: block;
    font-size: 20px;
    letter-spacing: 0;
    text-align: right;
    margin-top: 2px;
  }
  .brand--on-crimson { color: var(--paper); }

  .card--talvora-front .brand { left: 38px; top: 30px; font-size: 60px; }
  .card--quillpad-front .brand { left: 36px; top: 60px; font-size: 64px; }
  .card--quillpad-front .brand__sub { font-size: 18px; }
  .card--talvora-back .brand { left: 130px; top: 160px; font-size: 64px; }
  .card--quillpad-back .brand { left: 120px; top: 235px; font-size: 62px; }
  .card--quillpad-back .brand__sub { font-size: 17px; }

  .band {
    position: absolute;
    height: 30px;
    color: var(--paper);
    font-size: 22px;
    line-height: 30px;
    white-space: nowrap;
  }
  .band--name {
    left: 0; width: 290px;
    background: var(--lavender);
    clip-path: polygon(0 0, 100% 0, 93% 100%, 0 100%);
    padding-left: 44px;
  }
  .band--role {
    right: 0; width: 290px;
    background: var(--crimson);
    clip-path: polygon(8% 0, 100% 0, 100% 100%, 0 100%);
    padding-left: 40px;
  }
  .card--talvora-front .band--name { top: 150px; }
  .card--talvora-front .band--role { top: 188px; }
  .card--quillpad-front .band--name { top: 176px; }
  .card--quillpad-front .band--role { top: 212px; }

  .contact {
    position: absolute;
    left: 38px;
    bottom: 22px;
    font-size: 13px;
    font-style: normal;
    line-height: 21px;
    color: var(--ink-soft);
    white-space: nowrap;
  }
  .contact .sep { padding: 0 5px; }
</style>
</head>
<body>

<section class="card card--front card--talvora-front">
  <div class="backdrop backdrop--front" role="img" aria-label="Soft blush sunburst background"></div>
  <div class="brand">talvora<span class="brand__sub">group</span></div>
  <div class="band band--name">Dorian Sample</div>
  <div class="band band--role">Account Manager</div>
  <address class="contact">
    Level 17<span class="sep">|</span>482 Ormond Rd<span class="sep">|</span>North Sydney<span class="sep">|</span>NSW 2060<br>
    p: +61 2 5550 1738<span class="sep">|</span>f: +61 2 5550 1794<span class="sep">|</span>m: +61 4 00 555 012<br>
    example@talvoragroup.example.au<span class="sep">|</span>www.talvoragroup.example.au
  </address>
</section>

<section class="card card--back card--talvora-back">
  <div class="backdrop backdrop--back" role="img" aria-label="Crimson and lavender sunburst background"></div>
  <div class="brand brand--on-crimson">talvora<span class="brand__sub">group</span></div>
</section>

<section class="card card--front card--quillpad-front">
  <div class="backdrop backdrop--front" role="img" aria-label="Soft blush sunburst background"></div>
  <div class="brand">quillpad<span class="brand__sub">messaging solutions</span></div>
  <div class="band band--name">Dorian Sample</div>
  <div class="band band--role">Account Manager</div>
  <address class="contact">
    Level 17<span class="sep">|</span>482 Ormond Rd<span class="sep">|</span>North Sydney<span class="sep">|</span>NSW 2060<br>
    p: +61 2 5550 1738<span class="sep">|</span>f: +61 2 5550 1794<span class="sep">|</span>m: +61 4 00 555 012<br>
    example@talvoragroup.example.au<span class="sep">|</span>www.talvoragroup.example.au
  </address>
</section>

<section class="card card--back card--quillpad-back">
  <div class="backdrop backdrop--back" role="img" aria-label="Crimson and lavender sunburst background"></div>
  <div class="brand brand--on-crimson">quillpad<span class="brand__sub">messaging solutions</span></div>
</section>

</body>
</html>
```